THE PRACTICE NAME "The Renal Crest MD" FOR A NEW MEDICAL PRACTICE STARTUP

THIS IS A BUSINESS CARD REQUEST FOR A KIDNEY DOCTOR's(NEPHROLOGIST) PRACTICE, THIS PRACTICE WILL BE IN EL PASO,TEXAS USA.OPEN TO INNOVATIVE IDEAS!

THE RENAL CREST MD ( NAME OF PRACTICE)

VIKRANT L. MOTHRE, MD FNKF FASN ( NAME OF PHYSICIAN WITH DEGREES)
BOARD CERTIFIED INTERNAL MEDICINE
BOARD CERTIFIED NEPHROLOGY
HYPERTENSION SPECIALIST

OFFICE ADDRESS, PHONE, FAX AND EMAIL PENDING

Guarding Health. Building Futures.(MOTTO) THE LOGO SHOILD REFLECT THIS MESSAGE. WE NEED A LOGO DESIGN WITH 2 KIDNEYS OR CAN BE ONE KIDNEY ALSO.

Target Market(s)

PATIENTS WITH KIDNEY DISEASE, HYPERTENSION, ENGLISH AND SPANISH SPEAKING POPULATION AND PATIENTS ON DIALYSIS

Industry/Entity Type

Health Care

Contact Information for Business Card

HYPERTENSION SPECIALIST

WEBSITE URL PENDING

Font styles to use
Serif
Sans Serif
Script

Colors
fbed38
ffc214
fbf289
fbee3e
5c5c5c
333333
1b1b1b
757575
d3d3d3

Requirements
Must have
• A KIDNEY LOGO
• NAME OF THE PRACTICE
Nice to have
• IF THE CARD CAN BE IN THE SHAPE OF A KIDNEY

```html
<!DOCTYPE html>
<html lang="en">
<head>
<meta charset="utf-8">
<title>The Renal Crest MD – Business Card</title>
<link rel="stylesheet" href="https://fonts.googleapis.com/css2?family=Roboto+Condensed:wght@400;700&display=swap">
<style>
  :root {
    --gold: #fbf289;
    --gold-deep: #fbed38;
    --card: #1b1b1b;
    --card-edge: #333333;
    --bg: #d3d3d3;
  }
  * { box-sizing: border-box; margin: 0; padding: 0; }
  html, body { width: 1200px; height: 800px; overflow: hidden; }
  body {
    background: var(--bg);
    font-family: "Roboto Condensed", sans-serif;
    display: flex;
    align-items: center;
    justify-content: center;
    gap: 90px;
  }
  .card {
    width: 340px;
    height: 600px;
    background: var(--card);
    border-radius: 14px;
    box-shadow: 0 0 0 2px var(--card-edge);
    color: var(--gold);
    padding: 44px 32px;
    display: flex;
    flex-direction: column;
  }
  .brand {
    display: flex;
    align-items: center;
    gap: 18px;
  }
  .brand-mark {
    width: 130px;
    height: 130px;
    border-radius: 50%;
    background: var(--gold);
    flex: none;
  }
  .brand-name {
    font-weight: 700;
    font-size: 30px;
    line-height: 1.1;
    color: var(--gold);
  }
  .motto {
    margin-top: 22px;
    font-size: 18px;
    line-height: 1.35;
  }
  .icon-strip {
    width: 120px;
    height: 30px;
    border-radius: 6px;
    background: linear-gradient(90deg, var(--gold-deep), var(--gold));
    opacity: .85;
  }
  .divider {
    margin: 24px 0 26px;
    height: 2px;
    background: var(--gold);
  }
  .contact { list-style: none; display: flex; flex-direction: column; gap: 14px; margin-top: 24px; }
  .contact li { display: flex; align-items: center; gap: 12px; font-size: 15px; line-height: 1.3; }
  .contact svg { width: 18px; height: 18px; flex: none; fill: var(--gold); }
  .physician {
    font-weight: 700;
    font-size: 20px;
    line-height: 1.25;
    letter-spacing: .02em;
  }
  .degrees { font-weight: 400; font-size: 16px; display: block; }
  .credentials { margin-top: 12px; list-style: none; }
  .credentials li { font-size: 14px; letter-spacing: .02em; line-height: 1.8; white-space: nowrap; }
  .card-back .icon-strip { margin-top: auto; }
</style>
</head>
<body>

<section class="card card-front">
  <div class="brand">
    <span class="brand-mark"></span>
    <span class="brand-name">The Renal Crest MD</span>
  </div>
  <p class="motto">Guarding Health.<br>Building Futures. (MOTTO)</p>
  <div class="divider"></div>
  <div class="icon-strip" role="img" aria-label="Small kidney and person pictograms"></div>
  <ul class="contact">
    <li>
      <svg viewBox="0 0 24 24" aria-hidden="true"><path d="M12 2a7 7 0 0 0-7 7c0 5 7 13 7 13s7-8 7-13a7 7 0 0 0-7-7zm0 9.5A2.5 2.5 0 1 1 12 6.5a2.5 2.5 0 0 1 0 5z"/></svg>
      240 Mesa Crest Plaza, El Paso, Texas, USA
    </li>
    <li>
      <svg viewBox="0 0 24 24" aria-hidden="true"><path d="M6.6 10.8a15 15 0 0 0 6.6 6.6l2.2-2.2a1 1 0 0 1 1-.25 11.4 11.4 0 0 0 3.6.57 1 1 0 0 1 1 1V20a1 1 0 0 1-1 1A17 17 0 0 1 3 4a1 1 0 0 1 1-1h3.5a1 1 0 0 1 1 1c0 1.25.2 2.45.57 3.57a1 1 0 0 1-.25 1z"/></svg>
      0412 555 018
    </li>
    <li>
      <svg viewBox="0 0 24 24" aria-hidden="true"><path d="M6.6 10.8a15 15 0 0 0 6.6 6.6l2.2-2.2a1 1 0 0 1 1-.25 11.4 11.4 0 0 0 3.6.57 1 1 0 0 1 1 1V20a1 1 0 0 1-1 1A17 17 0 0 1 3 4a1 1 0 0 1 1-1h3.5a1 1 0 0 1 1 1c0 1.25.2 2.45.57 3.57a1 1 0 0 1-.25 1z"/></svg>
      0412 555 018
    </li>
    <li>
      <svg viewBox="0 0 24 24" aria-hidden="true"><path d="M3 5h18v14H3zm2 2v.5l7 4.5 7-4.5V7zm0 2.9V17h14V9.9l-7 4.5z"/></svg>
      renalcrestmd@mailbox.com
    </li>
  </ul>
</section>

<section class="card card-back">
  <div class="brand">
    <span class="brand-mark"></span>
    <span class="brand-name">The Renal Crest MD</span>
  </div>
  <div class="divider"></div>
  <p class="physician">VIKRANT L. MOTHRE<span class="degrees">MD FNKF FASN</span></p>
  <ul class="credentials">
    <li>BOARD CERTIFIED INTERNAL MEDICINE</li>
    <li>BOARD CERTIFIED NEPHROLOGY</li>
    <li>HYPERTENSION SPECIALIST</li>
  </ul>
  <div class="icon-strip" role="img" aria-label="Small kidney and person pictograms"></div>
</section>

</body>
</html>
```